Penwick Foot & Ankle Alderbrook Window Vinyl Cling

Hi,
I'm looking to get a window decal done, but need it professionally designed.
-must be 24" x 24"
-Quorum Font
-Include our logo, Podiatry, phone number and website
- The goal is to make this eye catching.
Thank you,
Warren

```html
<!DOCTYPE html>
<html lang="en">
<head>
<meta charset="utf-8">
<title>Penwick Foot &amp; Ankle Alderbrook – Window Cling 24 x 24</title>
<link href="https://fonts.googleapis.com/css2?family=Roboto+Condensed:wght@700;900&family=Arimo:wght@400&display=swap" rel="stylesheet">
<style>
  :root {
    --page: #ffffff;
    --ink: #000000;
    --orange: #f27f4a;
    --teal: #58c3a7;
    --panel-light: #ffffff;
    --panel-shade: #d2d2d5;
    --label: #1a1a1a;
  }
  html, body {
    margin: 0;
    padding: 0;
    width: 1200px;
    height: 1000px;
    overflow: hidden;
    background: var(--page);
  }
  .canvas {
    display: block;
    width: 1200px;
    height: 1000px;
  }
  .size-note {
    font-family: "Arimo", Arial, sans-serif;
    font-size: 22px;
    fill: var(--label);
  }
  .sign-frame { fill: var(--ink); }
  .logo-square { fill: var(--teal); }
  .brand-name {
    font-family: "Roboto Condensed", "Arial Narrow", sans-serif;
    font-weight: 900;
    fill: var(--orange);
  }
  .headline {
    font-family: "Roboto Condensed", "Arial Narrow", sans-serif;
    font-weight: 900;
    fill: var(--ink);
  }
  .divider { stroke: var(--ink); stroke-width: 3; }
  .tagline {
    font-family: "Roboto Condensed", "Arial Narrow", sans-serif;
    font-weight: 900;
    fill: var(--orange);
  }
  .phone {
    font-family: "Roboto Condensed", "Arial Narrow", sans-serif;
    font-weight: 900;
    fill: var(--ink);
  }
  .web-pill { fill: var(--ink); }
  .web-address {
    font-family: "Roboto Condensed", "Arial Narrow", sans-serif;
    font-weight: 700;
    fill: #ffffff;
  }
</style>
</head>
<body>
<svg class="canvas" viewBox="0 0 1200 1000" xmlns="http://www.w3.org/2000/svg">
  <defs>
    <radialGradient id="panelGlow" cx="0.42" cy="0.38" r="0.75">
      <stop offset="0" stop-color="#ffffff"/>
      <stop offset="0.55" stop-color="#ececee"/>
      <stop offset="1" stop-color="#d2d2d5"/>
    </radialGradient>
  </defs>

  <text class="size-note" x="968" y="111" text-anchor="end">Size: 24" x 24"</text>

  <g class="window-cling">
    <rect class="sign-frame" x="230" y="130" width="740" height="740"/>

    <g class="brand-block">
      <rect class="logo-square" x="268" y="180" width="130" height="130"/>
      <text class="brand-name" x="940" y="231" font-size="76" text-anchor="end" textLength="330" lengthAdjust="spacing">PENWICK</text>
      <text class="brand-name" x="940" y="297" font-size="76" text-anchor="end" textLength="484" lengthAdjust="spacingAndGlyphs">FOOT &amp; ANKLE</text>
      <text class="brand-name" x="940" y="340" font-size="51" text-anchor="end" textLength="300" lengthAdjust="spacingAndGlyphs">ALDERBROOK</text>
    </g>

    <rect class="info-panel" x="253" y="347" width="694" height="500" fill="url(#panelGlow)"/>

    <text class="headline" x="333" y="502" font-size="146" textLength="568" lengthAdjust="spacingAndGlyphs">PODIATRY</text>
    <line class="divider" x1="334" y1="537" x2="875" y2="537"/>
    <text class="tagline" x="267" y="623" font-size="73" textLength="665" lengthAdjust="spacingAndGlyphs">Foot &amp; Ankle Physicians</text>
    <text class="phone" x="323" y="726" font-size="86" textLength="554" lengthAdjust="spacingAndGlyphs">(877) 555-0142</text>

    <rect class="web-pill" x="396" y="761" width="408" height="68" rx="34" ry="34"/>
    <text class="web-address" x="600" y="811" font-size="54" text-anchor="middle" textLength="370" lengthAdjust="spacingAndGlyphs">StepWellFeet.com</text>
  </g>
</svg>
</body>
</html>
```